Homecare Information Flyer

We require a brochure/ leaflet to be created which would provide healthcare information to our staff and patients on the topic of- Pressure Ulcers. The document would ideally be 3 fold. It should include our Logo/ Company Information (Marlowe Staffing).

I have attached-
- Logo
- Text/ Visual images to be included.

Industry/Entity Type

Healthcare

```html
<!DOCTYPE html>
<html lang="en">
<head>
<meta charset="utf-8">
<title>Pressure Ulcers – Patient Information Leaflet</title>
<link href="https://fonts.googleapis.com/css2?family=Arimo:wght@400&family=Noto+Sans:wght@700&display=swap" rel="stylesheet">
<style>
  :root {
    --green: #8ab232;
    --green-text: #7aa52a;
    --shadow: #2f3a14;
    --body: #555555;
    --band-grey: #6a6a66;
    --paper: #ffffff;
  }
  * { box-sizing: border-box; margin: 0; padding: 0; }
  html, body { width: 1200px; height: 849px; overflow: hidden; background: var(--paper); }
  .leaflet { position: relative; width: 1200px; height: 849px; font-family: "Arimo", Arial, sans-serif; color: var(--body); font-size: 13px; line-height: 14.3px; }
  .panel { position: absolute; top: 36px; width: 345px; }
  .panel--left { left: 30px; line-height: 16px; }
  .panel--middle { left: 430px; }
  .panel--right { left: 830px; }
  .panel p, .panel ul { padding-left: 10px; }
  .section-title {
    position: relative; background: var(--green); color: #fff;
    font-family: "Noto Sans", Verdana, sans-serif; font-weight: 700;
    font-size: 12.5px; line-height: 14px; padding: 4px 10px 4px;
    width: 330px; height: 36px; box-shadow: 3px 3px 0 var(--shadow);
  }
  .panel--left .section-title { margin-bottom: 15px; }
  .panel--middle .section-title, .panel--right .section-title { margin-bottom: 10px; }
  .panel--left .subhead { margin-top: 16px; }
  .subhead { color: var(--green-text); margin-top: 14px; }
  .signs { list-style: none; margin-top: 14px; }
  .signs li { position: relative; padding-left: 18px; }
  .signs li::before { content: ""; position: absolute; left: 3px; top: 3px; width: 9px; height: 9px; background: var(--green); }
  .note { margin-top: 15px; }
  .caption { margin-top: 14px; }
  .diagram { margin-top: 6px; margin-left: 10px; }
  .diagram--back { width: 320px; height: 62px; background: linear-gradient(#f4f4f4, #e6e6e6); }
  .diagram--side { width: 320px; height: 88px; background: linear-gradient(#f4f4f4, #e6e6e6); }
  .diagram--chair { width: 256px; height: 216px; margin-left: 13px; margin-top: 8px; background: linear-gradient(#f7efe6, #ece4dc); box-shadow: 0 1px 4px rgba(0,0,0,.25); }
  .title--suspect { margin-top: 12px; }
  .contact { margin-top: 7px; }
  .contact a { color: #333; text-decoration: none; }
  .staff-photo { position: absolute; left: 928px; top: 634px; width: 272px; height: 215px; background: linear-gradient(160deg, #e9eef2 0%, #8fb3d9 55%, #4f84c0 100%); }
  .footer-band { position: absolute; left: 0; top: 808px; width: 1200px; height: 41px; background: linear-gradient(90deg, var(--band-grey) 0%, var(--band-grey) 55%, #dcdcdc 78%, #ffffff 90%); }
  .footer-band::before { content: ""; position: absolute; left: 0; top: 0; width: 40px; height: 41px; background: var(--green); }
</style>
</head>
<body>
<div class="leaflet">

  <div class="footer-band"></div>
  <div class="staff-photo" role="img" aria-label="Photograph of two smiling healthcare workers in blue scrubs, one holding a clipboard"></div>

  <section class="panel panel--left">
    <h2 class="section-title">Who is most at risk<br>of Developing Pressure Ulcers?</h2>
    <p>You may be at risk of developing pressure ulcers for<br>a number of reasons including the following:</p>
    <p class="subhead">Problems with Movement</p>
    <p>If your ability to move is limited you don't get enough<br>oxygen to the parts under pressure</p>
    <p class="subhead">Poor Circulation</p>
    <p>Vascular disease or smoking reduces your circulation</p>
    <p class="subhead">Moist Skin</p>
    <p>You may be at increased risk if your skin is too damp,<br>due to incontinence, sweat or a weeping wound.<br>It is important that your skin is kept clean and healthy.</p>
    <p class="subhead">Lack of Sensitivity to Pain of Discomfort</p>
    <p>Conditions such as Diabetes Stroke, Nerve, Muscle<br>Disorders, etc. reduce the normal sensations that<br>usually prompt you, or enable you to move. Some<br>treatments (e.g. Epidural pain relief, medications, and<br>operations) reduce your sensitivity to pain or<br>discomfort so that you are not aware of the need to<br>move.</p>
    <p class="subhead">Previous Tissue Damage</p>
    <p>Scar tissue will have lost some of its previous strength<br>and is more prone to breakdown.</p>
    <p class="subhead">Inadequate Diet of Fluid Intake</p>
    <p>Lack of fluid may dehydrate your tissues. Weight gain<br>or loss can affect the pressure distribution over bony<br>points and healing.</p>
    <p class="subhead">Risk Assessment</p>
    <p>To assess your risk of developing Pressure Ulcers,<br>a member of your Health Care team will examine/<br>assess you and ask you some questions. This will<br>help to identify if you require specialised equipment or<br>other forms of care, and will assist in providing for your<br>individual needs.</p>
  </section>

  <section class="panel panel--middle">
    <h2 class="section-title">What are the Early Signs of<br>a Pressure Ulcer?</h2>
    <p>You will notice the following signs:</p>
    <ul class="signs">
      <li>Change in skin colour redder or darker</li>
      <li>Heat or cold</li>
      <li>Discomfort or pain</li>
      <li>Blistering</li>
      <li>Skin damage</li>
    </ul>
    <p class="note">Without appropriate intervention the damage may<br>worsen, developing into hard black tissue or an open<br>wound.</p>
    <p class="subhead">Common Locations of Pressure Ulcers</p>
    <p class="caption">Laying on your back</p>
    <div class="diagram diagram--back" role="img" aria-label="Outline diagram of a person lying on their back, labelling back of head, shoulder blade, elbow, coccyx and heel as pressure points"></div>
    <p class="caption" style="margin-top:20px">Laying on your side</p>
    <div class="diagram diagram--side" role="img" aria-label="Outline diagram of a person lying on their side, labelling ear, shoulder and upper arm, elbow, hip, thigh, lower leg and heel and ankle"></div>
    <p class="caption" style="margin-top:22px">Sitting in a chair</p>
    <div class="diagram diagram--chair" role="img" aria-label="Illustration of a skeleton seated in a wheelchair with pressure points circled at scapula, elbow, sacrum, ischium, ball of foot and heel"></div>
  </section>

  <section class="panel panel--right">
    <h2 class="section-title">What can I do<br>to Avoid Pressure Ulcers?</h2>
    <p style="margin-top:14px">There are several ways you can reduce the risk of<br>pressure ulcers.</p>
    <p class="subhead">Keep Moving</p>
    <p>Changing your position regularly helps keep blood<br>flowing. If you have reduced movement the Health<br>Care team looking after you will assist you with regular<br>turns in addition to providing specialist mattresses,<br>cushions, boots etc.</p>
    <p class="subhead">Look for signs of Damage</p>
    <p>Check your skin for pressure damage at least once a<br>day. Look for skin that doesn't go back to its normal<br>colour after you have taken the weight off it. Do not<br>continue to lie on skin that is redder of darker than<br>usual. Also watch out for blisters, dry patches or<br>breaks in the skin.</p>
    <p class="subhead">Protect your Skin</p>
    <p>Wash your skin using warm water of PH Neutral skin<br>cleansers. Do not use heavily perfumed soap or<br>talcum powder as these can soak up the skins<br>natural oils leading to vulnerable dry areas. If you<br>suffer from incontinence please inform your health<br>care team as they can assess the best way to deal<br>with the problems. Rubbing/massaging skin is bad<br>for it.</p>
    <p class="subhead">Eat a Well-balanced Diet</p>
    <p>Make sure you eat a healthy balanced diet and drink<br>plenty of fluids. Extra protein may help.</p>
    <h2 class="section-title title--suspect">What should I do<br>if I suspect a pressure ulcer?</h2>
    <p class="contact">Tell your Doctor or Nurse as soon as possible and follow<br>the advice they give you Rhona Keller Clinical Nurse<br>Specialist at <a href="mailto:Rhona.keller@Marlowestaffing.co.uk">Rhona.keller@Marlowestaffing.co.uk</a></p>
  </section>

</div>
</body>
</html>
```